Dunlin Removals Junk Removal Postcard

I am looking to have a postcard made for my junk removal company. Details:
size: 6"x9"
I would like to keep it clean and simple. Our company colors are pink, blue and white. You can find the colors and info on the company and what we do on our website which is www.dunlinremovals-example.com .
I've attached a sample of a postcard that was made on ArtHive for another junk removal company. I like the way the attached one looks.

```html
<!DOCTYPE html>
<html lang="en">
<head>
<meta charset="utf-8">
<title>Dunlin Removals Postcard</title>
<link rel="stylesheet" href="https://fonts.googleapis.com/css2?family=Oswald:wght@400;500&family=Montserrat:wght@500;700;800&family=Signika:wght@400;600&family=Hind:wght@400&display=swap">
<style>
:root{
  --pink:#e3237f;
  --blue:#1f5fae;
  --deep-blue:#174e96;
  --white:#ffffff;
  --ice:#e4f1fb;
  --ink:#2b2b2b;
  --stage:#6eb2f2;
}
*{box-sizing:border-box;margin:0;padding:0}
html,body{width:1200px;height:1200px;overflow:hidden}
body{background:var(--stage);position:relative;font-family:"Signika",sans-serif}
.card{position:absolute;left:180px;width:840px;height:560px;background:var(--white);overflow:hidden}
.card--front{top:30px}
.card--back{top:610px}
.abs{position:absolute}

/* front */
.brand{display:flex;align-items:center;gap:10px;font-family:"Montserrat",sans-serif;font-weight:800;color:var(--blue);font-size:34px;white-space:nowrap}
.brand__dot{width:18px;height:18px;border-radius:50%;background:var(--pink);flex:none}
.front-brand{left:40px;top:62px}
.blue-panel{left:0;top:168px;width:540px;height:315px;background:var(--blue)}
.photo-disc{left:470px;top:-60px;width:600px;height:600px;border-radius:50%;border:7px solid var(--blue);
  background:linear-gradient(150deg,#d9dde2 0%,#f4f5f6 35%,#c8cdd3 55%,#2d5fb0 72%,#e3237f 88%)}
.headline{left:40px;top:178px;font-family:"Oswald",sans-serif;font-weight:500;color:var(--white);font-size:54px;line-height:1.06;letter-spacing:.5px}
.services{left:40px;top:308px;list-style:none;color:var(--white);font-weight:600;font-size:22px}
.services li{display:flex;align-items:center;gap:8px;height:42px}
.services svg{width:24px;height:24px}
.tagline{left:40px;top:448px;color:var(--white);font-size:15px;font-weight:400}
.pink-band{left:0;top:482px;width:840px;height:78px;background:var(--pink)}
.phone{font-family:"Montserrat",sans-serif;font-weight:700;color:var(--white);white-space:nowrap}
.front-phone{left:40px;top:488px;font-size:32px}
.front-url{left:40px;top:530px;font-family:"Montserrat",sans-serif;color:var(--white);font-size:15px;font-weight:500;white-space:nowrap}
.front-url b{font-weight:700}
.perks{left:398px;top:496px;width:420px;height:48px;background:var(--white);transform:skewX(-18deg);display:flex}
.perks div{flex:auto;display:flex;align-items:center;justify-content:center;border-right:3px solid var(--pink)}
.perks div:last-child{border:none}
.perks span{transform:skewX(18deg);font-family:"Montserrat",sans-serif;font-weight:500;color:var(--blue);font-size:12px;line-height:1.05;text-align:center;white-space:nowrap}
.ribbon{left:472px;top:408px;width:320px;height:54px;background:linear-gradient(90deg,#c81f73,var(--pink));transform:rotate(-4deg);display:flex;align-items:center;justify-content:center;
  font-family:"Montserrat",sans-serif;font-weight:800;color:var(--white);font-size:27px;letter-spacing:1px}

/* back */
.ice-panel{left:0;top:0;width:500px;height:560px;background:var(--ice)}
.banner{left:0;top:45px;width:518px;height:70px;background:var(--pink);color:var(--white);font-weight:600;font-size:19px;line-height:1.3;padding:9px 0 0 37px}
.back-title{left:37px;top:124px;font-family:"Oswald",sans-serif;font-weight:500;color:var(--blue);font-size:28px;white-space:nowrap}
.intro{left:37px;top:170px;width:450px;font-family:"Hind",sans-serif;color:var(--ink);font-size:15px;line-height:1.45;text-align:justify}
.options{left:37px;top:246px;display:grid;grid-template-columns:165px 140px;row-gap:4px;list-style:none;font-family:"Oswald",sans-serif;color:var(--ink);font-size:21px;font-weight:400}
.options li{display:flex;align-items:center;gap:8px}
.options li::before{content:"";width:14px;height:14px;border-radius:50%;background:var(--pink);box-shadow:inset 0 0 0 3px #f7a8cd}
.connect{left:0;top:357px;width:522px;height:72px;background:var(--blue);color:var(--white);font-family:"Montserrat",sans-serif;font-weight:800;font-size:25px;line-height:1.08;padding:7px 0 0 37px}
.pink-box{left:0;top:429px;width:500px;height:131px;background:var(--pink)}
.family-photo{left:340px;top:420px;width:160px;height:140px;background:linear-gradient(160deg,#c8589a,#8a5a68 55%,#d9a7b9)}
.back-phone{left:37px;top:434px;font-size:36px}
.socials{left:37px;top:490px;display:flex;gap:14px}
.socials i{width:20px;height:20px;border-radius:50%;background:var(--white);display:block}
.back-url{left:37px;top:524px;font-family:"Montserrat",sans-serif;color:var(--white);font-size:14px;font-weight:500;white-space:nowrap}
.back-url b{font-weight:700}
.back-brand{left:525px;top:70px;font-size:17px;gap:6px}
.back-brand .brand__dot{width:11px;height:11px}
.stamp{left:728px;top:45px;width:76px;height:80px;border:2px solid #111}
.address-line{left:555px;width:250px;height:1.5px;background:#111}
</style>
</head>
<body>

<section class="card card--front" aria-label="Postcard front">
  <div class="abs blue-panel"></div>
  <div class="abs photo-disc" role="img" aria-label="Photo of a white and pink refuse truck with a worker in blue and pink uniform beside a wheelie bin, junk pile behind"></div>
  <div class="abs brand front-brand"><span class="brand__dot"></span>Dunlin Removals</div>
  <h1 class="abs headline">RELAX, WE DO<br>THE DIRTY WORK</h1>
  <ul class="abs services">
    <li><svg viewBox="0 0 24 24" fill="none" stroke="#fff" stroke-width="1.6"><path d="M5 8h14l-1.5 13h-11z"/><path d="M3 8h18M9 8V4h6v4"/></svg>Junk, Rubbish, Trash, Hogwash</li>
    <li><svg viewBox="0 0 24 24" fill="none" stroke="#fff" stroke-width="1.6"><path d="M3 9l9-4 9 4-9 4z"/><path d="M3 9v8l9 4 9-4V9"/></svg>Clutter</li>
    <li><svg viewBox="0 0 24 24" fill="none" stroke="#fff" stroke-width="1.6"><rect x="3" y="7" width="18" height="14"/><path d="M7 7V3h10v4M8 12h8M8 16h8"/></svg>Debris, Scrap</li>
  </ul>
  <p class="abs tagline">whatever you're under, we're here to help clean it out.</p>
  <div class="abs ribbon">FREE ESTIMATE</div>
  <div class="abs pink-band"></div>
  <div class="abs phone front-phone">555-014-7328</div>
  <div class="abs front-url">www.<b>dunlinremovals-example</b>.com</div>
  <div class="abs perks">
    <div><span>CALL US</span></div>
    <div><span>SAME DAY<br>SERVICE</span></div>
    <div><span>FAST &amp;<br>PROFESSIONAL</span></div>
    <div><span>BEST<br>PRICE</span></div>
  </div>
</section>

<section class="card card--back" aria-label="Postcard back">
  <div class="abs ice-panel"></div>
  <div class="abs banner">Removing Junk for Residential + Commercial<br>clients across Northern VA</div>
  <h2 class="abs back-title">REMOVE THE JUNK RECLAIM YOUR SPACE</h2>
  <p class="abs intro">From lending a hand with your spring spruce up or pre-move prep to tackling robust construction clean outs and office-space overhauls, learn more about our "frequent fliers" here.</p>
  <ul class="abs options">
    <li>Residential</li><li>Curbside</li>
    <li>Commercial</li><li>Other</li>
    <li>Outside</li>
  </ul>
  <div class="abs connect">READY TO CLEAN IT OUT?<br>LET'S CONNECT</div>
  <div class="abs pink-box"></div>
  <div class="abs family-photo" role="img" aria-label="Photo of a smiling family of four hugging"></div>
  <div class="abs phone back-phone">555-014-7328</div>
  <div class="abs socials" aria-label="Social media links"><i></i><i></i><i></i><i></i></div>
  <div class="abs back-url">www.<b>dunlinremovals-example</b>.com</div>
  <div class="abs brand back-brand"><span class="brand__dot"></span>Dunlin Removals</div>
  <div class="abs stamp"></div>
  <div class="abs address-line" style="top:283px"></div>
  <div class="abs address-line" style="top:353px"></div>
  <div class="abs address-line" style="top:423px"></div>
</section>

</body>
</html>
```